Silver Kettle Studio Marketing Postcard

I need a 2 sided A6 postcard to distribute to potential clients. The postcard will include the business logo and information about the service we provide and contact information. I want it to be stylish and to compliment the business card. I've attached the business card and logo files as well as some text to use. I have other source files (.eps and.ai) if required please message me. I don't need the postal address or my position included on the postcard.
I am open to portrait or landscape designs, whatever you think is most stylish and eye catching.

```html
<!DOCTYPE html>
<html lang="en">
<head>
<meta charset="utf-8">
<title>Silver Kettle Studio – Technology Explained Postcard</title>
<link href="https://fonts.googleapis.com/css2?family=Jura:wght@400;500&display=swap" rel="stylesheet">
<style>
  :root {
    --navy: #07263a;
    --ink-light: #e9eef1;
  }
  html, body {
    margin: 0;
    padding: 0;
    width: 1200px;
    height: 848px;
    overflow: hidden;
    background: var(--navy);
  }
  .postcard {
    position: relative;
    width: 1200px;
    height: 848px;
    background: var(--navy);
    color: var(--ink-light);
    font-family: "Jura", "Trebuchet MS", sans-serif;
    text-transform: uppercase;
    text-align: center;
    overflow: hidden;
  }
  .postcard__title {
    position: absolute;
    top: 45px;
    left: 0;
    width: 100%;
    margin: 0;
    font-size: 34px;
    line-height: 40px;
    font-weight: 500;
    letter-spacing: 1px;
  }
  .postcard__body {
    position: absolute;
    top: 134px;
    left: 0;
    width: 100%;
    font-size: 25px;
    line-height: 35px;
    font-weight: 500;
    letter-spacing: 0.6px;
  }
  .postcard__body p,
  .postcard__body ul {
    margin: 0;
    padding: 0;
    list-style: none;
  }
  .services {
    margin-bottom: 35px !important;
  }
  .services li::before {
    content: "•";
  }
</style>
</head>
<body>
  <main class="postcard">
    <h1 class="postcard__title">Technology Explained</h1>
    <div class="postcard__body">
      <p class="intro">
        Do you feel frustrated by computers, TVs, phones,<br>
        tablets and countless other digital devices?<br>
        Silver Kettle Studio is here to help. From a<br>
        simple computer health<br>
        check to the purchase and installation of home networks<br>
        and digital services. We also give useful product<br>
        advice and maintenance tips.
      </p>
      <ul class="services">
        <li>On site support</li>
        <li>Advice</li>
        <li>Installation</li>
        <li>Education</li>
      </ul>
      <p class="contact">
        Let us help you tame your digital world.<br>
        Phone conversations are free so call Rowan<br>
        on 0400 555 318<br>
        Email: rowan@silverkettle.com.au<br>
        or go to<br>
        www.silverkettle.com.au<br>
        for more information problems solved.
      </p>
    </div>
  </main>
</body>
</html>
```